Solar energy proposal for homeowners

I am providing households with solar energy proposals, and I need a high-quality brochure that is packaged cleverly to attract the homeowner's attention. Take a look at the one page solar brochure that I have included to get an idea of text and content.

Target Market(s)

Residential Homeowners

Industry/Entity Type

Solar

Requirements
Must have
• High quality document

```html
<!DOCTYPE html>
<html lang="en">
<head>
<meta charset="utf-8">
<title>Brightwell Energy – Solar Rental Flyer</title>
<link href="https://fonts.googleapis.com/css2?family=Anton&family=Montserrat:wght@600&family=Questrial&display=swap" rel="stylesheet">
<style>
  :root{
    --stage:#e6e4df;
    --brand-blue:#0f8ac4;
    --headline-blue:#1c9ad8;
    --lime:#9cbd22;
    --lime-soft:#cfe3a2;
    --ink:#3a3a3a;
    --ink-dark:#1f2a1a;
    --body-green:#6c8a3c;
    --white:#ffffff;
    --shade:rgba(40,30,20,.55);
    --hero-warm:#b98a5a;
    --hero-cool:#3f6f92;
    --crew-tone:#8a9aac;
  }
  *{box-sizing:border-box;margin:0;padding:0}
  html,body{width:1040px;height:1200px;overflow:hidden;background:var(--stage)}
  body{position:relative;font-family:"Questrial",sans-serif}
  .flyer{position:absolute;left:70px;top:18px;width:900px;height:1163px;background:var(--white);overflow:hidden;box-shadow:0 8px 24px rgba(0,0,0,.18)}
  .hero-photo{position:absolute;left:0;top:0;width:900px;height:650px;
    background:linear-gradient(180deg,var(--hero-warm) 0%,var(--hero-cool) 55%,var(--white) 100%);}
  .brand{position:absolute;left:560px;top:66px;display:flex;align-items:center;gap:12px;white-space:nowrap}
  .brand-square{width:46px;height:46px;background:var(--brand-blue)}
  .brand-name{font-family:"Questrial",sans-serif;font-size:34px;color:#5fb33a;letter-spacing:.5px}
  .headline{position:absolute;left:48px;top:188px;font-family:"Anton",sans-serif;color:var(--headline-blue);line-height:1;-webkit-text-stroke:1px #0b3b5a;font-weight:400}
  .headline span{display:inline-block;background:var(--shade);padding:4px 16px 6px 16px;font-size:62px;letter-spacing:3px;white-space:nowrap}
  .headline span+span{display:block;width:558px}
  .hero-bar{position:absolute;left:64px;top:339px;width:94px;height:11px;background:var(--lime)}
  .hero-text{position:absolute;left:64px;top:371px;width:475px;font-size:12.5px;line-height:15.5px;color:var(--white)}
  .feature{position:absolute;top:491px;width:178px;height:203px;background:var(--brand-blue);color:var(--white);box-shadow:0 3px 6px rgba(0,0,0,.2)}
  .feature-icon{position:absolute;top:-30px;left:44px;width:90px;height:90px;border-radius:50%;background:var(--brand-blue);border:2px solid var(--white);display:flex;align-items:center;justify-content:center}
  .feature-title{position:absolute;top:84px;left:11px;right:8px;font-family:"Anton",sans-serif;font-size:15px;line-height:18px;letter-spacing:.2px;font-weight:400}
  .feature-bar{position:absolute;left:11px;width:46px;height:5px;background:var(--lime)}
  .feature-text{position:absolute;left:11px;right:10px;font-size:12px;line-height:14px}
  .green-band{position:absolute;left:0;top:884px;width:900px;height:210px;background:var(--lime-soft)}
  .crew-photo{position:absolute;left:13px;top:697px;width:392px;height:392px;border-radius:50%;
    background:var(--crew-tone);
    box-shadow:0 0 0 4px var(--white), 0 0 0 6px rgba(255,255,255,.5)}
  .pitch{position:absolute;left:470px;top:728px;font-family:"Montserrat",sans-serif;font-weight:600;font-size:29px;line-height:37px;color:var(--ink)}
  .pitch-bar{position:absolute;left:470px;top:851px;width:46px;height:5px;background:var(--lime)}
  .pitch-text{position:absolute;left:470px;top:904px;width:320px;font-size:11.6px;line-height:14.2px;color:var(--body-green);text-align:justify}
  .footer{position:absolute;left:0;top:1094px;width:900px;height:69px;background:var(--lime);color:var(--ink-dark);font-size:12px;line-height:14px}
  .footer-address{position:absolute;left:38px;top:14px}
  .footer-web{position:absolute;left:315px;top:35px;font-size:15px;letter-spacing:6px}
  .footer-contact{position:absolute;left:684px;top:30px}
</style>
</head>
<body>
<main class="flyer">
  <div class="hero-photo" role="img" aria-label="Sunset over a large field of solar panels"></div>

  <div class="brand">
    <div class="brand-square"></div>
    <div class="brand-name">brightwell energy</div>
  </div>

  <h1 class="headline"><span>CUT YOUR</span><span>ELECTRICITY BILL BY</span></h1>
  <div class="hero-bar"></div>
  <p class="hero-text">Brightwell Energy installs and maintains high-efficiency solar systems at our own expense. You pay a flat monthly rental fee. No debt, no liens, just cheaper electricity. Click on our FAQ's to understand how the process works.</p>

  <section class="features">
    <article class="feature" style="left:72px">
      <div class="feature-icon">
        <svg width="56" height="56" viewBox="0 0 56 56" fill="none" stroke="#fff" stroke-width="2" stroke-linecap="round" stroke-linejoin="round">
          <circle cx="30" cy="16" r="10"/>
          <path d="M30 10v12M33 12.5c-1-1.5-5-1.8-5.5.3-.5 2.4 6 1.8 5.5 4.5-.4 2.2-4.6 2-5.8.4"/>
          <path d="M6 36h8l8-3h10c2 0 2 3 0 3h-8M14 44h16l14-9c2-1.2 0-4-2-3l-10 5"/>
          <rect x="3" y="34" width="6" height="12"/>
        </svg>
      </div>
      <h2 class="feature-title" style="top:92px">No Money Out of Pocket</h2>
      <div class="feature-bar" style="top:122px"></div>
      <p class="feature-text" style="top:141px;font-size:13px;line-height:16px;right:30px">Start saving from day one.</p>
    </article>
    <article class="feature" style="left:270px">
      <div class="feature-icon">
        <svg width="56" height="56" viewBox="0 0 56 56" fill="none" stroke="#fff" stroke-width="2" stroke-linecap="round" stroke-linejoin="round">
          <path d="M20 33c-4-3-5-7-5-10a13 13 0 0 1 26 0c0 3-1 7-5 10v5H20z"/>
          <path d="M22 42h12M24 46h8M28 38V22M28 30c-5-2-5-8 0-11 5 3 5 9 0 11"/>
          <path d="M28 4v3M10 10l2 2M46 10l-2 2M6 24h3M47 24h3"/>
        </svg>
      </div>
      <h2 class="feature-title" style="right:40px">Guaranteed Energy Production</h2>
      <div class="feature-bar" style="top:122px"></div>
      <p class="feature-text" style="top:139px;right:20px">You only rely on a system that performs. We credit you for any shortages.</p>
    </article>
    <article class="feature" style="left:470px">
      <div class="feature-icon">
        <svg width="56" height="56" viewBox="0 0 56 56" fill="none" stroke="#fff" stroke-width="2" stroke-linecap="round" stroke-linejoin="round">
          <path d="M16 8h19l7 7v33H16z"/><path d="M35 8v7h7"/>
          <path d="M21 20h16M21 25h16M21 30h16M21 35h16M21 40h12"/>
        </svg>
      </div>
      <h2 class="feature-title" style="left:14px;right:70px">Simple Rental Agreement</h2>
      <div class="feature-bar" style="top:122px;left:14px"></div>
      <p class="feature-text" style="top:139px;left:14px">Flexible terms for homes and businesses.</p>
    </article>
    <article class="feature" style="left:665px">
      <div class="feature-icon">
        <svg width="56" height="56" viewBox="0 0 56 56" fill="none" stroke="#fff" stroke-width="2" stroke-linecap="round" stroke-linejoin="round">
          <path d="M10 24a18 18 0 0 1 32-10M46 32a18 18 0 0 1-32 10"/>
          <path d="M42 7v7h-7M14 49v-7h7"/>
          <path d="M28 40V28M28 30c-7 0-9-5-9-9 6 0 9 3 9 9M28 28c0-6 3-9 9-9 0 4-2 9-9 9"/>
        </svg>
      </div>
      <h2 class="feature-title" style="top:92px">Sustainable Impact</h2>
      <div class="feature-bar" style="top:120px"></div>
      <p class="feature-text" style="top:137px;right:25px">Reduce your carbon footprint effortlessly.</p>
    </article>
  </section>

  <div class="green-band"></div>
  <div class="crew-photo" role="img" aria-label="Aerial view of two installers in hard hats walking between rooftop solar panels"></div>

  <h2 class="pitch">Because solar should<br>be simple, transparent,<br>and risk-free.</h2>
  <div class="pitch-bar"></div>
  <p class="pitch-text">Brightwell Energy is redefining how people and businesses access solar. We are not here to sell you power. We are here to help you generate your own. With guaranteed performance, full system maintenance, and flexible rental terms, you can power your property with total peace of mind and none of the long-term financial commitments of traditional solar.</p>

  <footer class="footer">
    <div class="footer-address">Brightwell Energy, LLC<br>4120 Harbor Pine Road<br>Tampa, FL 33602</div>
    <div class="footer-web">brightwellenergy.com</div>
    <div class="footer-contact">(p) 555.014.2290<br>(e) info@brightwellenergy.com</div>
  </footer>
</main>
</body>
</html>
```